Redesign of business card for Birchline Mechanical

We are looking for a new design for our business cards for Birchline Mechanical. We are a plumbing & HVAC construction company, operating on the West Coast of Canada and USA. Logo attached.
Industry/Entity Type
Construction - Plumbing & HVAC
Contact Information for Business Card
Name, address, phone numbers, email, website address
Look and feel
Each slider illustrates characteristics of the customer's brand and the style your logo design should communicate.

```html
<!DOCTYPE html>
<html lang="en">
<head>
<meta charset="utf-8">
<title>Birchline Mechanical – Business Card</title>
<link rel="stylesheet" href="https://fonts.googleapis.com/css2?family=Arimo:wght@400;700&display=swap">
<style>
  :root {
    --bg: #e4e5e7;
    --card: #ffffff;
    --ink: #1b1b1b;
    --muted: #8a8a8a;
    --frame: #1a1a1a;
  }
  * { margin: 0; padding: 0; box-sizing: border-box; }
  html, body { width: 1200px; height: 800px; overflow: hidden; }
  body {
    background: var(--bg);
    font-family: "Arimo", Arial, sans-serif;
    color: var(--ink);
    display: flex;
    align-items: center;
    justify-content: center;
    gap: 50px;
  }
  .card {
    position: relative;
    width: 540px;
    height: 310px;
    background: var(--card);
    box-shadow: 0 6px 18px rgba(0,0,0,0.12);
  }
  .card-frame { position: absolute; inset: 0; }
  .card-content { position: absolute; inset: 0; }

  /* Brand name (replaces logo) */
  .brand {
    display: flex;
    align-items: center;
    gap: 10px;
    font-size: 17px;
    font-weight: 700;
    letter-spacing: 1px;
    color: var(--ink);
    text-transform: uppercase;
  }
  .brand-mark {
    width: 16px; height: 16px;
    background: var(--ink);
    flex: none;
  }

  /* Front */
  .front .contact {
    position: absolute;
    left: 46px; top: 88px;
  }
  .person-name {
    font-size: 15px; font-weight: 700; letter-spacing: 0.5px;
    text-transform: uppercase;
  }
  .person-title {
    font-size: 13px; color: var(--muted); margin-top: 3px; margin-bottom: 12px;
  }
  .contact-row {
    display: flex; align-items: center; gap: 8px;
    font-size: 13px; color: #444; margin-bottom: 5px;
  }
  .contact-row svg { width: 12px; height: 12px; flex: none; }
  .contact-footer {
    position: absolute; left: 46px; bottom: 58px;
    display: flex; align-items: center; gap: 12px;
    font-size: 13px; color: #444;
  }
  .contact-footer .divider { width: 1px; height: 34px; background: #777; }
  .address { line-height: 1.35; }
  .front .brand { position: absolute; right: 46px; top: 138px; }

  /* Back */
  .back .card-content {
    display: flex; flex-direction: column; align-items: center;
    padding-top: 92px;
  }
  .services-title {
    margin-top: 36px;
    font-size: 13px; font-weight: 700; letter-spacing: 0.5px;
    text-transform: uppercase;
  }
  .services-list {
    list-style: none; text-align: center; margin-top: 6px;
    font-size: 13px; line-height: 1.35; color: var(--muted);
  }
</style>
</head>
<body>

  <!-- Front side -->
  <section class="card front" aria-label="Business card front">
    <svg class="card-frame" viewBox="0 0 540 310" aria-hidden="true">
      <g stroke="var(--frame)" stroke-width="9" fill="none">
        <line x1="14" y1="12" x2="190" y2="12"/>
        <line x1="200" y1="12" x2="526" y2="12"/>
        <line x1="14" y1="298" x2="340" y2="298"/>
        <line x1="350" y1="298" x2="526" y2="298"/>
        <line x1="14" y1="12" x2="14" y2="150"/>
        <line x1="14" y1="160" x2="14" y2="298"/>
        <line x1="526" y1="12" x2="526" y2="150"/>
        <line x1="526" y1="160" x2="526" y2="298"/>
      </g>
    </svg>
    <div class="card-content">
      <div class="contact">
        <p class="person-name">Dalton Reyes</p>
        <p class="person-title">President/Founder</p>
        <p class="contact-row">
          <svg viewBox="0 0 12 12"><path d="M2.5 1h2l1 3-1.5 1a7 7 0 0 0 3 3l1-1.5 3 1v2a1 1 0 0 1-1 1A10 10 0 0 1 1.5 2a1 1 0 0 1 1-1z" fill="var(--ink)"/></svg>
          213-555-0148
        </p>
        <p class="contact-row">
          <svg viewBox="0 0 12 12"><rect x="0.5" y="2" width="11" height="8" fill="var(--ink)"/><path d="M1 2.5l5 4 5-4" stroke="#fff" stroke-width="1" fill="none"/></svg>
          info@birchlinemech.com
        </p>
        <p class="contact-row">
          <svg viewBox="0 0 12 12"><g stroke="var(--ink)" stroke-width="1" fill="none"><circle cx="6" cy="6" r="5"/><ellipse cx="6" cy="6" rx="2.2" ry="5"/><line x1="1" y1="6" x2="11" y2="6"/></g></svg>
          www.birchlinemech.com
        </p>
      </div>
      <div class="contact-footer">
        <span class="divider"></span>
        <p class="address">8250 Harbor Mill Rd. S<br>Suite #117 Tacoma, WA 98402</p>
      </div>
      <div class="brand"><span class="brand-mark"></span>Birchline Mechanical</div>
    </div>
  </section>

  <!-- Back side -->
  <section class="card back" aria-label="Business card back">
    <svg class="card-frame" viewBox="0 0 540 310" aria-hidden="true">
      <g stroke="var(--frame)" stroke-width="9" fill="none">
        <line x1="14" y1="12" x2="190" y2="12"/>
        <line x1="200" y1="12" x2="526" y2="12"/>
        <line x1="14" y1="298" x2="340" y2="298"/>
        <line x1="350" y1="298" x2="526" y2="298"/>
        <line x1="14" y1="12" x2="14" y2="150"/>
        <line x1="14" y1="160" x2="14" y2="298"/>
        <line x1="526" y1="12" x2="526" y2="150"/>
        <line x1="526" y1="160" x2="526" y2="298"/>
      </g>
    </svg>
    <div class="card-content">
      <div class="brand"><span class="brand-mark"></span>Birchline Mechanical</div>
      <p class="services-title">Our Services</p>
      <ul class="services-list">
        <li>Pipefitting Systems / Design Build / Maintenance</li>
        <li>Fire Protection / Control Systems</li>
        <li>Energy Recovery &amp; High Efficiency Systems</li>
        <li>Plumbing / HVAC</li>
      </ul>
    </div>
  </section>

</body>
</html>
```